Kickgrid Numbers Service

We have a football stats service that we feel would benefit from some design input. In particular we would like the designer to look at three pages. We will then transfer this style across the rest of the site.

We are looking for designs for three pages. Links to the existing pages we would like reworked are:

Player:
http://demostats.kickgrid-example.com/Player.asp?lang=&coid=4&teid=220&plid=197404

Team Stats:
http://demostats.kickgrid-example.com/Team_Stats.asp?lang=&coid=4&teid=218

League Table:
http://demostats.kickgrid-example.com/Comp_Table.asp?lang=&coid=4

We require the page structure to remain as is with the main country/competition selector on the left and the content on the right.

The colour palette, fonts, content separators etc are all in your hands. We will use this version as a sales tool for our services. In many cases this will be restyled to match a specific clients requirements.

We are happy for this to be done in HTML/CSS or as a layered image file.

Target Market(s)

These stats pages are for use on newspaper and bookmaker websites.

Industry/Entity Type

Sales

Requirements
Nice to have
• A nice colour palette for graphs and charts is important.

```html
<!DOCTYPE html>
<html lang="en">
<head>
<meta charset="utf-8">
<title>Team Stats Screen – Kickgrid Numbers Service</title>
<link href="https://fonts.googleapis.com/css2?family=Open+Sans:wght@300;400;600;700&display=swap" rel="stylesheet">
<style>
:root{
  --bar-dark:#2e323d;
  --sidebar:#4a5263;
  --sidebar-band:#3c4350;
  --sidebar-line:#555d6d;
  --sidebar-text:#d3d7de;
  --orange:#ee5a2f;
  --blue:#2f80d9;
  --yellow:#f5c000;
  --header-bg:#efeee8;
  --panel-border:#dcdcdc;
  --row-alt:#f3f3f3;
  --text:#333a44;
  --muted:#7b808a;
  --red:#cc2e3a;
  --maroon:#6e2c33;
  --grey-bar:#8a8a8a;
  --green:#3c9a35;
  --title-grey:#b7b4b5;
}
*{box-sizing:border-box;margin:0;padding:0}
html,body{width:1200px;height:3237px;overflow:hidden}
body{
  font-family:"Open Sans",Arial,sans-serif;color:var(--text);
  background:linear-gradient(100deg,#d3d0d2 0%,#e6e3e4 45%,#f4e6df 80%,#efe3e1 100%);
  position:relative;
}
.board-title{position:absolute;top:50px;left:0;width:1200px;text-align:center;font-size:46px;font-weight:400;letter-spacing:2px;color:var(--title-grey)}
.frame{position:absolute;left:123px;top:160px;width:952px;height:2920px;background:#fff;box-shadow:0 4px 18px rgba(0,0,0,.18);overflow:hidden}
.topbar{position:absolute;left:0;top:0;width:952px;height:54px;background:var(--bar-dark);color:#fff}
.topbar .date{position:absolute;left:22px;top:17px;font-size:14px}
.mode{position:absolute;top:17px;font-size:14px;color:#d6d8dc;display:flex;align-items:center;gap:6px}
.radio{width:14px;height:14px;border-radius:50%;background:#fff;display:inline-block;position:relative}
.radio.on::after{content:"";position:absolute;left:4px;top:4px;width:6px;height:6px;border-radius:50%;background:var(--orange)}
.search-field{position:absolute;left:619px;top:14px;width:214px;height:26px;background:#fff;border:1px solid #ccc;font-size:11px;color:#aaa;padding:5px 8px}
.search-btn{position:absolute;left:842px;top:13px;width:88px;height:28px;background:var(--yellow);color:var(--bar-dark);font-size:13px;font-weight:600;display:flex;align-items:center;justify-content:center;gap:5px}
.sidebar{position:absolute;left:0;top:54px;width:201px;height:2842px;background:var(--sidebar);color:var(--sidebar-text)}
.today-btn{position:absolute;left:22px;top:30px;width:146px;height:28px;background:var(--orange);color:#fff;font-size:11px;font-weight:700;display:flex;align-items:center;justify-content:center;gap:6px;border-radius:2px}
.side-band{position:absolute;left:0;width:201px;height:32px;background:var(--sidebar-band);font-size:12.5px;font-weight:600;padding:8px 22px;color:#e3e6ea;border-top:1px solid #5d6576;border-bottom:1px solid #5d6576}
.side-list{position:absolute;left:0;width:201px;list-style:none}
.side-list li{height:33.5px;border-bottom:1px solid var(--sidebar-line);font-size:13.5px;padding:7px 22px;display:flex;align-items:center;gap:10px}
.flag{width:22px;height:14px;display:inline-block;flex:none}
.more-btn{position:absolute;left:22px;width:78px;height:28px;background:var(--blue);color:#fff;font-size:13px;font-weight:600;border-radius:3px;display:flex;align-items:center;justify-content:center;gap:6px}
.plus{width:16px;height:16px;border-radius:50%;background:#fff;color:var(--blue);font-size:14px;font-weight:700;line-height:16px;text-align:center}
.player-head{position:absolute;left:201px;top:54px;width:751px;height:101px;background:var(--header-bg)}
.player-badge{position:absolute;left:28px;top:20px;width:60px;height:60px}
.player-name{position:absolute;left:114px;top:24px;font-size:24px;color:#222}
.player-comp{position:absolute;left:114px;top:58px;font-size:14px;color:#444;display:flex;align-items:center;gap:8px}
.menu-btn{position:absolute;left:685px;top:32px;width:41px;height:33px;background:#ddd;border:1px solid #c6c6c6;border-radius:3px;display:flex;flex-direction:column;align-items:center;justify-content:center;gap:3px}
.menu-btn span{width:18px;height:3px;background:#555}
.footbar{position:absolute;left:0;top:2896px;width:952px;height:24px;background:var(--bar-dark)}
.panel{position:absolute;left:224px;width:702px;border:1px solid var(--panel-border);background:#fff}
.panel-head{height:35px;background:var(--bar-dark);color:#fff;font-size:12.5px;font-weight:600;padding:9px 14px;text-transform:uppercase;letter-spacing:.2px}
.panel svg{display:block}
.split{display:flex}
.split>div{width:351px}
.split>div+div{border-left:1px solid var(--panel-border)}
.split .panel-head{border-right:1px solid #444a57}
.games{list-style:none}
.games li{height:39px;position:relative;font-size:14px;border-bottom:1px solid #e8e8e8}
.games li:nth-child(even){background:var(--row-alt)}
.games .kit{position:absolute;top:8px;width:22px;height:22px;border-radius:4px}
.games .home{position:absolute;left:62px;top:10px}
.games .score{position:absolute;left:280px;top:10px;font-weight:700}
.games .when{position:absolute;left:330px;top:12px;font-size:11.5px;color:#666}
.games .away{position:absolute;right:86px;top:10px}
.stats-table{width:100%;border-collapse:collapse;font-size:14px}
.stats-table th{height:39px;text-align:left;font-weight:700;font-size:13px;color:#333}
.stats-table td{height:39px}
.stats-table tr:nth-child(even) td{background:var(--row-alt)}
.stats-table .c1{padding-left:24px;width:334px}
.stats-table .c2{width:222px}
.axis{font-size:9.5px;fill:#444;font-family:"Open Sans",Arial,sans-serif}
.legend{font-size:10.5px;fill:#333;font-family:"Open Sans",Arial,sans-serif}
</style>
</head>
<body>
<div class="board-title">TEAM STATS SCREEN</div>

<div class="frame">
  <header class="topbar">
    <div class="date">25 September 2014</div>
    <div class="mode" style="left:434px"><span class="radio"></span>Teams</div>
    <div class="mode" style="left:529px"><span class="radio on"></span>Players</div>
    <div class="search-field">Search</div>
    <div class="search-btn">
      <svg width="14" height="14" viewBox="0 0 14 14"><circle cx="5.5" cy="5.5" r="4" fill="none" stroke="#2e323d" stroke-width="2"/><line x1="8.5" y1="8.5" x2="13" y2="13" stroke="#2e323d" stroke-width="2"/></svg>Search
    </div>
  </header>

  <nav class="sidebar">
    <div class="today-btn">TODAY'S MATCHES <span style="width:12px;height:12px;border-radius:50%;background:#fff;color:var(--orange);font-size:9px;line-height:12px;text-align:center">›</span></div>
    <div class="side-band" style="top:62px">DOMESTIC FOOTBALL</div>
    <ul class="side-list" style="top:94px">
      <li><svg class="flag" viewBox="0 0 3 2"><rect width="1" height="2" fill="#1f3f9a"/><rect x="1" width="1" height="2" fill="#fff"/><rect x="2" width="1" height="2" fill="#d62a2a"/></svg>France</li>
      <li><svg class="flag" viewBox="0 0 3 3"><rect width="3" height="1" fill="#111"/><rect y="1" width="3" height="1" fill="#d52a1e"/><rect y="2" width="3" height="1" fill="#f5c400"/></svg>Germany</li>
      <li><svg class="flag" viewBox="0 0 3 2"><rect width="1" height="2" fill="#23913f"/><rect x="1" width="1" height="2" fill="#fff"/><rect x="2" width="1" height="2" fill="#cf2b37"/></svg>Italy</li>
      <li><svg class="flag" viewBox="0 0 20 12"><rect width="20" height="12" fill="#1f3f9a"/><path d="M0 0L20 12M20 0L0 12" stroke="#fff" stroke-width="2.4"/></svg>Spain</li>
      <li><svg class="flag" viewBox="0 0 3 4"><rect width="3" height="1" fill="#c60b1e"/><rect y="1" width="3" height="2" fill="#ffc400"/><rect y="3" width="3" height="1" fill="#c60b1e"/></svg>Scotland</li>
      <li><svg class="flag" viewBox="0 0 20 12"><rect width="20" height="12" fill="#fff"/><rect x="8.3" width="3.4" height="12" fill="#cf2b37"/><rect y="4.3" width="20" height="3.4" fill="#cf2b37"/></svg>England</li>
    </ul>
    <div class="more-btn" style="top:488px"><span class="plus">+</span>More</div>
    <div class="side-band" style="top:524px">CONTINENTAL FOOTBALL</div>
    <ul class="side-list" style="top:558px">
      <li>Champions Cup</li>
      <li>Champ Cup Qual.</li>
      <li>Continental League</li>
      <li>Continental League Qual.</li>
    </ul>
    <div class="more-btn" style="top:719px"><span class="plus">+</span>More</div>
  </nav>

  <section class="player-head">
    <svg class="player-badge" viewBox="0 0 60 60"><circle cx="30" cy="30" r="29" fill="#fff" stroke="#e0e0e0"/><rect x="25" y="1" width="10" height="58" fill="#d9303a"/><rect x="1" y="25" width="58" height="10" fill="#d9303a"/></svg>
    <h1 class="player-name" style="font-weight:400">Dario Kovalenko</h1>
    <div class="player-comp"><svg width="18" height="12" viewBox="0 0 20 12"><rect width="20" height="12" fill="#fff" stroke="#ddd"/><rect x="8.3" width="3.4" height="12" fill="#cf2b37"/><rect y="4.3" width="20" height="3.4" fill="#cf2b37"/></svg>Premier Division</div>
    <div class="menu-btn"><span></span><span></span><span></span></div>
  </section>

  <!-- Match by match performance -->
  <section class="panel" style="top:177px;height:282px">
    <div class="panel-head">Match by Match Performance : 2014 - 2015</div>
    <svg width="700" height="245" viewBox="0 0 700 245">
      <defs><linearGradient id="redBar" x1="0" y1="0" x2="0" y2="1"><stop offset="0" stop-color="#e1464f"/><stop offset="1" stop-color="#c12834"/></linearGradient></defs>
      <rect x="83" y="34" width="548" height="159" fill="#f6f6f6" stroke="#ccc"/>
      <g stroke="#e2e2e2"><line x1="83" y1="60.5" x2="631" y2="60.5"/><line x1="83" y1="113.5" x2="631" y2="113.5"/><line x1="83" y1="140" x2="631" y2="140"/><line x1="83" y1="166.5" x2="631" y2="166.5"/></g>
      <line x1="83" y1="87" x2="631" y2="87" stroke="#888"/>
      <g fill="url(#redBar)">
        <rect x="139" y="60.5" width="86" height="26.5"/>
        <rect x="229" y="84.5" width="86" height="2.5"/>
        <rect x="316" y="60.5" width="86" height="26.5"/>
        <rect x="406" y="60.5" width="86" height="26.5"/>
        <rect x="495" y="87" width="86" height="79.5"/>
      </g>
      <g class="axis" text-anchor="end"><text x="76" y="37">2</text><text x="76" y="64">1</text><text x="76" y="90">0</text><text x="76" y="117">-1</text><text x="76" y="143">-2</text><text x="76" y="170">-3</text><text x="76" y="196">-4</text></g>
      <g class="axis" text-anchor="middle"><text x="182" y="208">1</text><text x="272" y="208">2</text><text x="359" y="208">3</text><text x="449" y="208">4</text><text x="538" y="208">5</text><text x="357" y="224">Match</text></g>
      <text class="axis" transform="translate(60 113) rotate(-90)" text-anchor="middle">Goal Difference</text>
    </svg>
  </section>

  <!-- Last 6 games -->
  <section class="panel" style="top:485px;height:270px">
    <div class="panel-head">Last 6 Games</div>
    <ul class="games">
      <li><span class="kit" role="img" aria-label="Ashford Vale kit" style="left:16px;background:#8a2d45"></span><span class="home">Ashford Vale</span><span class="score">0-3</span><span class="when">20 September 2014 - 15:00</span><span class="away">Harbour Town</span><span class="kit" role="img" aria-label="Harbour Town kit" style="right:22px;background:#e23a3a"></span></li>
      <li><span class="kit" role="img" aria-label="Mersey Rovers kit" style="left:16px;background:#e23a3a"></span><span class="home">Mersey Rovers</span><span class="score">0-1</span><span class="when">13 September 2014 - 17:30</span><span class="away">Ashford Vale</span><span class="kit" role="img" aria-label="Ashford Vale kit" style="right:22px;background:#8a2d45"></span></li>
      <li><span class="kit" role="img" aria-label="Ashford Vale kit" style="left:16px;background:#8a2d45"></span><span class="home">Ashford Vale</span><span class="score">2-1</span><span class="when">31 August 2014 - 13:30</span><span class="away">Humber City</span><span class="kit" role="img" aria-label="Humber City kit" style="right:22px;background:#c98a1e"></span></li>
      <li><span class="kit" role="img" aria-label="Ashford Vale kit" style="left:16px;background:#8a2d45"></span><span class="home">Ashford Vale</span><span class="score">0-0</span><span class="when">23 August 2014 - 12:45</span><span class="away">Tynebridge United</span><span class="kit" role="img" aria-label="Tynebridge United kit" style="right:22px;background:#555"></span></li>
      <li><span class="kit" role="img" aria-label="Potter City kit" style="left:16px;background:#e86060"></span><span class="home">Potter City</span><span class="score">0-1</span><span class="when">16 August 2014 - 15:00</span><span class="away">Ashford Vale</span><span class="kit" role="img" aria-label="Ashford Vale kit" style="right:22px;background:#8a2d45"></span></li>
      <li><span class="kit" role="img" aria-label="Whitlow Athletic kit" style="left:16px;background:#e9e9e9;border:1px solid #ccc"></span><span class="home">Whitlow Athletic</span><span class="score">3-0</span><span class="when">11 May 2014 - 15:00</span><span class="away">Ashford Vale</span><span class="kit" role="img" aria-label="Ashford Vale kit" style="right:22px;background:#8a2d45"></span></li>
    </ul>
  </section>

  <!-- League position analysis -->
  <section class="panel" style="top:783px;height:302px">
    <div class="panel-head">League Position Analysis</div>
    <svg width="700" height="265" viewBox="0 0 700 265">
      <rect x="84" y="32" width="547" height="151" fill="#fff" stroke="#bbb"/>
      <g stroke="#e4e4e4">
        <path d="M84 40.4H631M84 48.8H631M84 57.2H631M84 65.6H631M84 74H631M84 82.3H631M84 90.7H631M84 99.1H631M84 107.5H631M84 115.9H631M84 124.3H631M84 132.7H631M84 141.1H631M84 149.4H631M84 157.8H631M84 166.2H631M84 174.6H631"/>
        <path d="M98.8 32V183M113.6 32V183M128.3 32V183M143.1 32V183M157.9 32V183M172.7 32V183M187.5 32V183M202.2 32V183M217 32V183M231.8 32V183M246.6 32V183M261.4 32V183M276.1 32V183M290.9 32V183M305.7 32V183M320.5 32V183M335.3 32V183M350 32V183M364.8 32V183M379.6 32V183M394.4 32V183M409.2 32V183M423.9 32V183M438.7 32V183M453.5 32V183M468.3 32V183M483.1 32V183M497.8 32V183M512.6 32V183M527.4 32V183M542.2 32V183M557 32V183M571.7 32V183M586.5 32V183M601.3 32V183M616.1 32V183"/>
      </g>
      <polyline fill="none" stroke="#bdbdbd" stroke-width="2" points="84,107.5 98.8,174.6 113.6,183 128.3,149.4 157.9,149.4 187.5,166.2 217,166.2 246.6,166.2 276.1,157.8 305.7,149.4 335.3,141.1 364.8,157.8 394.4,149.4 423.9,157.8 453.5,149.4 483.1,149.4 512.6,157.8 542.2,166.2 571.7,149.4 601.3,132.7 630.9,141.1"/>
      <polyline fill="none" stroke="#555" stroke-width="2" points="84,32 98.8,82.3 128.3,157.8 157.9,82.3 187.5,115.9 217,115.9 246.6,82.3 276.1,115.9 305.7,82.3 335.3,82.3 364.8,115.9 394.4,115.9 423.9,82.3 453.5,82.3 483.1,107.5 512.6,115.9 542.2,132.7 571.7,149.4 601.3,132.7 630.9,149.4"/>
      <polyline fill="none" stroke="#d92b2b" stroke-width="2.5" points="84,32 98.8,48.8 113.6,40.4 128.3,32"/>
      <g class="axis" text-anchor="end"><text x="78" y="35">2</text><text x="78" y="52">4</text><text x="78" y="69">6</text><text x="78" y="86">8</text><text x="78" y="102">10</text><text x="78" y="119">12</text><text x="78" y="136">14</text><text x="78" y="153">16</text><text x="78" y="170">18</text><text x="78" y="186">20</text></g>
      <g class="axis" text-anchor="middle"><text x="98.8" y="197">2</text><text x="128.3" y="197">4</text><text x="157.9" y="197">6</text><text x="187.5" y="197">8</text><text x="217" y="197">10</text><text x="246.6" y="197">12</text><text x="276.1" y="197">14</text><text x="305.7" y="197">16</text><text x="335.3" y="197">18</text><text x="364.8" y="197">20</text><text x="394.4" y="197">22</text><text x="423.9" y="197">24</text><text x="453.5" y="197">26</text><text x="483.1" y="197">28</text><text x="512.6" y="197">30</text><text x="542.2" y="197">32</text><text x="571.7" y="197">34</text><text x="601.3" y="197">36</text><text x="630.9" y="197">38</text><text x="357" y="210">Games Played</text></g>
      <text class="axis" transform="translate(58 107) rotate(-90)" text-anchor="middle">League Position</text>
      <g class="legend"><rect x="232" y="219" width="18" height="3" fill="#bdbdbd"/><text x="255" y="224">2012 - 2013</text><rect x="322" y="219" width="18" height="3" fill="#555"/><text x="345" y="224">2013 - 2014</text><rect x="412" y="219" width="18" height="3" fill="#d92b2b"/><text x="435" y="224">2014 - 2015</text></g>
    </svg>
  </section>

  <!-- Results & scores -->
  <section class="panel split" style="top:1113px;height:235px">
    <div>
      <div class="panel-head">League Results Analysis : 2014 - 2015</div>
      <svg width="350" height="198" viewBox="0 0 350 198">
        <g transform="rotate(-90 129 95)">
          <circle cx="129" cy="95" r="34.5" fill="none" stroke="#3c9a35" stroke-width="69" pathLength="100" stroke-dasharray="60 40"/>
          <circle cx="129" cy="95" r="34.5" fill="none" stroke="#d83a3a" stroke-width="69" pathLength="100" stroke-dasharray="0 60 20 20"/>
          <circle cx="129" cy="95" r="34.5" fill="none" stroke="#f6e63e" stroke-width="69" pathLength="100" stroke-dasharray="0 80 20 0"/>
        </g>
        <g class="legend">
          <rect x="196" y="45" width="11" height="9" fill="#3c9a35"/><text x="212" y="53">Wins</text>
          <rect x="196" y="60" width="11" height="9" fill="#d83a3a"/><text x="212" y="68">Losses</text>
          <rect x="196" y="75" width="11" height="9" fill="#f09a2a"/><text x="212" y="83">Score Draws</text>
          <rect x="196" y="90" width="11" height="9" fill="#f6e63e"/><text x="212" y="98">No Score Draws</text>
        </g>
      </svg>
    </div>
    <div>
      <div class="panel-head">Popular Scores (Last 20 Games)</div>
      <svg width="350" height="198" viewBox="0 0 350 198">
        <g transform="rotate(-90 207 95)" fill="none" stroke-width="69">
          <circle cx="207" cy="95" r="34.5" stroke="#1ba9be" pathLength="100" stroke-dasharray="14 86"/>
          <circle cx="207" cy="95" r="34.5" stroke="#8cc43f" pathLength="100" stroke-dasharray="0 14 14 72"/>
          <circle cx="207" cy="95" r="34.5" stroke="#9a9a9a" pathLength="100" stroke-dasharray="0 28 12 60"/>
          <circle cx="207" cy="95" r="34.5" stroke="#cfd3da" pathLength="100" stroke-dasharray="0 40 10 50"/>
          <circle cx="207" cy="95" r="34.5" stroke="#4d4d4d" pathLength="100" stroke-dasharray="0 50 10 40"/>
          <circle cx="207" cy="95" r="34.5" stroke="#c5dca0" pathLength="100" stroke-dasharray="0 60 9 31"/>
          <circle cx="207" cy="95" r="34.5" stroke="#8fc7d4" pathLength="100" stroke-dasharray="0 69 7 24"/>
          <circle cx="207" cy="95" r="34.5" stroke="#2f65a6" pathLength="100" stroke-dasharray="0 76 24 0"/>
        </g>
        <g class="legend">
          <rect x="284" y="24" width="11" height="9" fill="#1ba9be"/><text x="300" y="32">1 - 4</text>
          <rect x="284" y="39" width="11" height="9" fill="#8cc43f"/><text x="300" y="47">1 - 0</text>
          <rect x="284" y="54" width="11" height="9" fill="#9a9a9a"/><text x="300" y="62">0 - 0</text>
          <rect x="284" y="69" width="11" height="9" fill="#cfd3da"/><text x="300" y="77">1 - 2</text>
          <rect x="284" y="84" width="11" height="9" fill="#4d4d4d"/><text x="300" y="92">0 - 3</text>
          <rect x="284" y="99" width="11" height="9" fill="#c5dca0"/><text x="300" y="107">0 - 2</text>
          <rect x="284" y="114" width="11" height="9" fill="#8fc7d4"/><text x="300" y="122">0 - 1</text>
          <rect x="284" y="129" width="11" height="9" fill="#2f65a6"/><text x="300" y="137">Other</text>
        </g>
      </svg>
    </div>
  </section>

  <!-- Double result -->
  <section class="panel" style="top:1379px;height:306px">
    <div class="panel-head">Double Result (Last 20 Games)</div>
    <svg width="700" height="269" viewBox="0 0 700 269">
      <rect x="142" y="42" width="495" height="164" fill="#f7f7f7" stroke="#ccc"/>
      <g stroke="#e1e1e1"><path d="M224.5 42V206M307 42V206M389.5 42V206M472 42V206M554.5 42V206"/></g>
      <g fill="#6e2c33">
        <rect x="142" y="46" width="330" height="11"/>
        <rect x="142" y="64" width="165" height="11"/>
        <rect x="142" y="119" width="247.5" height="11"/>
        <rect x="142" y="173" width="82.5" height="11"/>
        <rect x="142" y="191" width="412.5" height="11"/>
        <rect x="142" y="209" width="0" height="0"/>
      </g>
      <rect x="142" y="191" width="412.5" height="11" fill="#6e2c33"/>
      <g class="axis" text-anchor="end">
        <text x="136" y="55">Win / Win</text><text x="136" y="73">Draw / Win</text><text x="136" y="91">Loss / Win</text>
        <text x="136" y="110">Win / Draw</text><text x="136" y="128">Draw / Draw</text><text x="136" y="146">Loss / Draw</text>
        <text x="136" y="164">Win / Loss</text><text x="136" y="182">Draw / Loss</text><text x="136" y="200">Loss / Loss</text>
      </g>
      <g class="axis" text-anchor="middle"><text x="224.5" y="220">1</text><text x="307" y="220">2</text><text x="389.5" y="220">3</text><text x="472" y="220">4</text><text x="554.5" y="220">5</text><text x="389.5" y="235">Games</text></g>
      <text class="axis" transform="translate(76 124) rotate(-90)" text-anchor="middle">Double Result</text>
    </svg>
  </section>

  <!-- Total goals per game -->
  <section class="panel" style="top:1711px;height:304px">
    <div class="panel-head">Total Goals per Game (Last 20 Games)</div>
    <svg width="700" height="267" viewBox="0 0 700 267">
      <rect x="80" y="30" width="546" height="162" fill="#f7f7f7" stroke="#ccc"/>
      <g stroke="#e1e1e1"><path d="M80 48H626M80 66H626M80 84H626M80 102H626M80 120H626M80 138H626M80 156H626M80 174H626"/></g>
      <g fill="#6e2c33">
        <rect x="88" y="30" width="22" height="162"/><rect x="149" y="48" width="22" height="144"/>
        <rect x="210" y="174" width="22" height="18"/><rect x="270" y="174" width="22" height="18"/>
        <rect x="331" y="174" width="22" height="18"/>
      </g>
      <g fill="#8a8a8a">
        <rect x="114" y="138" width="22" height="54"/><rect x="175" y="102" width="22" height="90"/>
        <rect x="236" y="174" width="22" height="18"/><rect x="296" y="102" width="22" height="90"/>
        <rect x="357" y="156" width="22" height="36"/><rect x="418" y="120" width="22" height="72"/>
      </g>
      <g class="axis" text-anchor="end"><text x="73" y="195">0</text><text x="73" y="177">1</text><text x="73" y="159">2</text><text x="73" y="141">3</text><text x="73" y="123">4</text><text x="73" y="105">5</text><text x="73" y="87">6</text><text x="73" y="69">7</text><text x="73" y="51">8</text><text x="73" y="33">9</text></g>
      <g class="axis" text-anchor="middle"><text x="111" y="207">0</text><text x="171" y="207">1</text><text x="232" y="207">2</text><text x="293" y="207">3</text><text x="353" y="207">4</text><text x="414" y="207">5</text><text x="474" y="207">6</text><text x="535" y="207">7</text><text x="596" y="207">8+</text><text x="353" y="220">Goals</text></g>
      <text class="axis" transform="translate(58 111) rotate(-90)" text-anchor="middle">Games</text>
      <g class="legend"><rect x="284" y="226" width="10" height="9" fill="#6e2c33"/><text x="298" y="234">Ashford Vale</text><rect x="370" y="226" width="10" height="9" fill="#8a8a8a"/><text x="384" y="234">Match Total</text></g>
    </svg>
  </section>

  <!-- Time of first goal -->
  <section class="panel" style="top:2043px;height:305px">
    <div class="panel-head">Time of 1st Goal (Last 20 Games)</div>
    <svg width="700" height="268" viewBox="0 0 700 268">
      <rect x="76" y="49" width="548" height="145" fill="#f7f7f7" stroke="#ccc"/>
      <g stroke="#e1e1e1"><path d="M76 78H624M76 107H624M76 136H624M76 165H624"/></g>
      <g fill="#3aa335">
        <rect x="92" y="107" width="16" height="87"/><rect x="153" y="136" width="16" height="58"/><rect x="214" y="136" width="16" height="58"/>
        <rect x="275" y="165" width="16" height="29"/><rect x="336" y="165" width="16" height="29"/><rect x="458" y="165" width="16" height="29"/><rect x="580" y="165" width="16" height="29"/>
      </g>
      <g fill="#e0413f">
        <rect x="109" y="136" width="16" height="58"/><rect x="170" y="136" width="16" height="58"/><rect x="231" y="136" width="16" height="58"/>
        <rect x="292" y="165" width="16" height="29"/><rect x="353" y="165" width="16" height="29"/><rect x="475" y="136" width="16" height="58"/>
        <rect x="536" y="107" width="16" height="87"/><rect x="597" y="165" width="16" height="29"/>
      </g>
      <g fill="#3a3ad6">
        <rect x="126" y="49" width="16" height="145"/><rect x="187" y="107" width="16" height="87"/><rect x="248" y="136" width="16" height="58"/>
        <rect x="309" y="136" width="16" height="58"/><rect x="370" y="136" width="16" height="58"/><rect x="492" y="136" width="16" height="58"/>
        <rect x="553" y="165" width="16" height="29"/><rect x="614" y="136" width="10" height="58"/>
      </g>
      <g class="axis" text-anchor="end"><text x="69" y="197">0</text><text x="69" y="168">1</text><text x="69" y="139">2</text><text x="69" y="110">3</text><text x="69" y="81">4</text><text x="69" y="52">5</text></g>
      <g class="axis" text-anchor="middle"><text x="117" y="208">10</text><text x="178" y="208">20</text><text x="239" y="208">30</text><text x="300" y="208">40</text><text x="361" y="208">50</text><text x="422" y="208">60</text><text x="483" y="208">70</text><text x="544" y="208">80</text><text x="605" y="208">FT</text><text x="350" y="221">Minutes 1st goal scored within</text></g>
      <text class="axis" transform="translate(56 121) rotate(-90)" text-anchor="middle">Games</text>
      <g class="legend"><rect x="224" y="226" width="10" height="9" fill="#3aa335"/><text x="238" y="234">1st Goal For</text><rect x="318" y="226" width="10" height="9" fill="#e0413f"/><text x="332" y="234">1st Goal Against</text><rect x="428" y="226" width="10" height="9" fill="#3a3ad6"/><text x="442" y="234">1st Goal Any</text></g>
    </svg>
  </section>

  <!-- Average statistics -->
  <section class="panel" style="top:2378px;height:427px">
    <div class="panel-head">Average Statistics : 2014 - 2015</div>
    <table class="stats-table">
      <thead><tr><th class="c1"></th><th class="c2">HOME</th><th>AWAY</th></tr></thead>
      <tbody>
        <tr><td class="c1">Goals scored</td><td>0.7</td><td>1</td></tr>
        <tr><td class="c1">Goals conceded</td><td>1.3</td><td>0</td></tr>
        <tr><td class="c1">Time first goal scored</td><td>14 mins</td><td>30 mins</td></tr>
        <tr><td class="c1">Time first goal conceded</td><td>53 mins</td><td>-</td></tr>
        <tr><td class="c1">Yellow cards</td><td>2</td><td>2</td></tr>
        <tr><td class="c1">Red cards</td><td>0</td><td>0</td></tr>
        <tr><td class="c1">Subs used</td><td>3</td><td>2.5</td></tr>
        <tr><td class="c1">Biggest victory</td><td>2-1</td><td>1-0</td></tr>
        <tr><td class="c1">Biggest defeat</td><td>3-0</td><td>-</td></tr>
      </tbody>
    </table>
  </section>

  <footer class="footbar"></footer>
</div>
</body>
</html>
```